Brindlewick Solutions - Website for a CRM IT Services Provider to Non-profits

We need a website design for our company that provides IT services to non-profits to enable them to manage their donors and philanthropy within their organization.

We would like to see a design that uses the colors in our logo and a funky take on how to uniquely present a topic as boring as IT. Examples of sites that we really like: tamsinvoke.com, www.corabellquist.com, mintgable.com

The final design should communicate that we are a professional, yet creative company that is fun to work with.

Target Market(s)

Non-profits who tend to be young, creative types that are low-tech

Industry/Entity Type

It Company

Requirements
Must have
• Must include tabs for Home, Contact Us, About, Projects, and Blog. The site must use the logo we have attached on all of the page, in one way or another (it can be small & in the corner).

The site has to work on all mobile browsers (iphone, ipad).
Nice to have
• It would be great if I could supply some HTML for the Contact page that would allow me to capture leads and put them directly into my CRM application. It's very easy to set up.
Should not have
• The design should not use old-style fonts and should not have a lot of dark colors. Keep it similar to our logo, clean and simple. We're not looking for a busy home page.

```html
<!DOCTYPE html>
<html lang="en">
<head>
<meta charset="utf-8">
<title>Brindlewick Solutions</title>
<link rel="stylesheet" href="https://fonts.googleapis.com/css2?family=Gelasio:wght@400;500&display=swap">
<style>
  :root {
    --teal: #3599a9;
    --teal-tab: #2d8392;
    --teal-deep: #1c6470;
    --teal-ink: #1f5c67;
    --teal-text: #2a7b88;
    --line: #23707c;
    --paper: #efefef;
    --white: #ffffff;
    --grey-text: #7a7a7a;
    --follow: #555555;
  }
  * { box-sizing: border-box; margin: 0; padding: 0; }
  html, body { width: 1200px; height: 996px; overflow: hidden; }
  body {
    position: relative;
    background: var(--paper);
    font-family: "Gelasio", Georgia, serif;
  }
  .top-strip { position: absolute; left: 0; top: 0; width: 1200px; height: 5px; background: var(--teal-tab); }

  .brand { position: absolute; left: 110px; top: 13px; width: 150px; text-align: center; }
  .brand-mark { width: 86px; height: 86px; border-radius: 50%; background: var(--teal-tab); margin: 0 auto; }
  .brand-name { margin-top: 6px; font-size: 16px; color: var(--teal-text); white-space: nowrap; }

  .main-nav {
    position: absolute; left: 551px; top: 0; width: 529px; height: 40px;
    background: var(--teal-tab); border-radius: 0 0 8px 8px;
    display: flex; overflow: hidden;
  }
  .main-nav a {
    color: var(--white); text-decoration: none; font-size: 18px; letter-spacing: 0.6px;
    line-height: 40px; padding: 0 20px; white-space: nowrap;
  }
  .main-nav a.is-active { background: var(--teal-deep); padding: 0 20px 0 34px; width: 105px; }

  .follow { position: absolute; left: 786px; top: 60px; display: flex; align-items: center; }
  .follow-label { font-size: 18px; color: var(--follow); margin-right: 22px; }
  .social { width: 36px; height: 36px; border-radius: 7px; margin-right: 14px; }
  .social--one { background: #3c6ea3; }
  .social--two { background: #5db6df; }
  .social--three { background: #c84a45; }
  .social--four { background: #e98d35; margin-right: 0; }

  .search-tab { position: absolute; left: 782px; top: 122px; }
  .search-field {
    position: absolute; left: 830px; top: 130px; width: 207px; height: 18px;
    background: var(--white); border: 1px solid var(--line);
  }
  .search-field svg { position: absolute; right: 3px; top: 1px; }

  .hero {
    position: absolute; left: 0; top: 151px; width: 1200px; height: 565px;
    background: var(--teal); border-top: 3px solid var(--line);
  }
  .hero-visual {
    position: absolute; left: 150px; top: 20px; width: 491px; height: 315px;
    border: 1px solid var(--line);
    background: linear-gradient(135deg, #f2f3f3 0%, #d4d7d8 55%, #a9aeb0 100%);
  }
  .hero-title {
    position: absolute; left: 690px; top: 66px; width: 480px; white-space: nowrap;
    font-size: 40px; line-height: 56px; font-weight: 400; letter-spacing: 1px; color: var(--teal-ink);
  }
  .hero-shadow {
    position: absolute; left: 230px; top: 358px; width: 750px; height: 14px;
    background: radial-gradient(ellipse at center top, rgba(20,60,70,.55), rgba(20,60,70,0) 70%);
  }
  .slider-dots { position: absolute; left: 552px; top: 376px; display: flex; gap: 9px; }
  .slider-dots span { width: 12px; height: 12px; border-radius: 50%; background: #e4eef0; }
  .slider-dots span.is-current { background: var(--teal-deep); }

  .services {
    position: absolute; left: 0; top: 716px; width: 1200px; height: 211px;
    background: var(--white);
  }
  .service-badge {
    position: absolute; top: 574px; width: 230px; height: 230px; border-radius: 50%;
    background: var(--white); border: 1px solid var(--line);
  }
  .service-icon {
    position: absolute; left: 70px; top: 34px; width: 90px; height: 104px; border-radius: 12px;
  }
  .icon-data { background: linear-gradient(180deg, #d9dcde, #8e9599 60%, #2b8fc2); }
  .icon-support { background: linear-gradient(180deg, #c9302c 0%, #c9302c 25%, #c7cacc 26%, #eeeeee 100%); }
  .icon-network { background: linear-gradient(180deg, #2b6bc9, #f3cf6a 45%, #e2b043); }
  .icon-internet { background: linear-gradient(180deg, #244fa6, #6b8fd6 55%, #dfe3e8); }
  .service-text {
    position: absolute; top: 736px; width: 230px; text-align: center;
  }
  .service-text h2 {
    font-size: 24px; line-height: 24px; font-weight: 400; letter-spacing: 1px; color: var(--teal-text);
  }
  .service-text p {
    margin-top: 13px; font-size: 14px; line-height: 20px; letter-spacing: 0.3px;
    color: var(--grey-text); padding: 0 22px;
  }
  .service-text a {
    display: block; margin-top: 21px; font-size: 14px; letter-spacing: 0.3px;
    color: var(--teal-text); text-decoration: none;
  }

  .site-footer {
    position: absolute; left: 0; top: 927px; width: 1200px; height: 69px;
    border-top: 1px solid #cfcfcf; text-align: center;
    font-size: 14px; color: var(--grey-text); padding-top: 10px;
  }
</style>
</head>
<body>
  <div class="top-strip"></div>

  <div class="brand">
    <div class="brand-mark"></div>
    <div class="brand-name">Brindlewick Solutions</div>
  </div>

  <nav class="main-nav">
    <a class="is-active" href="#">Home</a>
    <a href="#">Contact Us</a>
    <a href="#">About</a>
    <a href="#">Projects</a>
    <a href="#">Blog</a>
  </nav>

  <div class="follow">
    <span class="follow-label">follow us :</span>
    <span class="social social--one"></span>
    <span class="social social--two"></span>
    <span class="social social--three"></span>
    <span class="social social--four"></span>
  </div>

  <svg class="search-tab" width="304" height="31" viewBox="0 0 304 31">
    <path d="M0 30 L28 4 Q32 0 38 0 L266 0 Q272 0 276 4 L304 30 Z" fill="var(--teal-tab)"/>
  </svg>
  <div class="search-field">
    <svg width="16" height="14" viewBox="0 0 16 14">
      <circle cx="6" cy="6" r="4.5" fill="none" stroke="#1c6470" stroke-width="1.6"/>
      <line x1="9.5" y1="9" x2="14.5" y2="13" stroke="#1c6470" stroke-width="2"/>
    </svg>
  </div>

  <section class="hero">
    <div class="hero-visual" role="img" aria-label="Photo of a white keyboard with a silver and green globe resting on the keys"></div>
    <h1 class="hero-title">Use information<br>technology to<br>meet your<br>business objectives</h1>
    <div class="hero-shadow"></div>
    <div class="slider-dots">
      <span></span><span></span><span class="is-current"></span><span></span><span></span>
    </div>
  </section>

  <div class="service-badge" style="left:120px"><div class="service-icon icon-data" role="img" aria-label="Icon of a database cylinder with a blue globe"></div></div>
  <div class="service-badge" style="left:363px"><div class="service-icon icon-support" role="img" aria-label="Icon of a support technician in a red cap and white shirt"></div></div>
  <div class="service-badge" style="left:606px"><div class="service-icon icon-network" role="img" aria-label="Icon of a folder linked to networked computers"></div></div>
  <div class="service-badge" style="left:849px"><div class="service-icon icon-internet" role="img" aria-label="Icon of a blue globe with a network cable"></div></div>

  <section class="services"></section>

  <div class="service-text" style="left:120px">
    <h2>Web<br>Development</h2>
    <p>Eibudamet aut rerum odes necessitatibus saepe evenievoluptates estu repudiandae sint et mole.</p>
    <a href="#">Learn more...</a>
  </div>
  <div class="service-text" style="left:363px">
    <h2>Technical<br>Support</h2>
    <p>Eibudamet aut rerum odes necessitatibus saepe evenievoluptates estu repudiandae sint et mole.</p>
    <a href="#">Learn more...</a>
  </div>
  <div class="service-text" style="left:606px">
    <h2>Network<br>Solutions</h2>
    <p>Eibudamet aut rerum odes necessitatibus saepe evenievoluptates estu repudiandae sint et mole.</p>
    <a href="#">Learn more...</a>
  </div>
  <div class="service-text" style="left:849px">
    <h2>Internet<br>Solutions</h2>
    <p>Eibudamet aut rerum odes necessitatibus saepe evenievoluptates estu repudiandae sint et mole.</p>
    <a href="#">Learn more...</a>
  </div>

  <footer class="site-footer"><p>Copyright @ 2012</p></footer>
</body>
</html>
```